Standard Biz Card
Health Professionals
Please upload ai or eps of your logo
Kindly upload logo file in ai/eps format!
That contest is here: http://orders.markcraftplaza.example/contests/new-health-clinic-logo-biz-card
Sorry, there seem to be a misunderstandig as we thought this job was combined with the logo job. We do not have a logo yet, it is another contest going on at the moment.
Please upload the logo files

```html
<!DOCTYPE html>
<html lang="en">
<head>
<meta charset="utf-8">
<title>Health Professionals Business Card</title>
<link rel="stylesheet" href="https://fonts.googleapis.com/css2?family=PT+Sans+Narrow:wght@400;700&family=Ubuntu:wght@700&display=swap">
<style>
  :root {
    --gold: #f0c62f;
    --gold-deep: #c99a12;
    --gold-light: #f7dc6a;
    --paper: #ffffff;
  }
  html, body {
    margin: 0;
    padding: 0;
    overflow: hidden;
    background: var(--paper);
  }
  .card {
    position: relative;
    width: 1200px;
    height: 686px;
    background: var(--paper);
    overflow: hidden;
  }
  .card__band {
    position: absolute;
    inset: 0;
  }
  .card__emblem {
    position: absolute;
    left: 840px;
    top: 90px;
    width: 340px;
    height: 540px;
    border-radius: 50%;
    background: radial-gradient(ellipse at center, var(--gold-light) 0%, var(--gold-deep) 45%, rgba(240,198,47,0) 72%);
  }
  .logo-box {
    position: absolute;
    left: 60px;
    top: 60px;
    width: 175px;
    height: 175px;
    background: var(--gold);
    display: flex;
    align-items: center;
    justify-content: center;
  }
  .logo-box__name {
    font-family: "Ubuntu", sans-serif;
    font-weight: 700;
    font-size: 34px;
    line-height: 1.25;
    color: var(--paper);
    text-align: center;
    letter-spacing: 1px;
  }
  .identity {
    position: absolute;
    left: 632px;
    top: 52px;
    margin: 0;
    padding: 0;
    list-style: none;
    font-family: "Ubuntu", sans-serif;
    font-weight: 700;
    font-size: 30px;
    line-height: 46px;
    letter-spacing: 2px;
    color: var(--paper);
  }
  .contact {
    position: absolute;
    left: 60px;
    top: 392px;
    margin: 0;
    font-family: "PT Sans Narrow", sans-serif;
    font-size: 39px;
    line-height: 51px;
    color: var(--gold);
    display: grid;
    grid-template-columns: 140px auto;
  }
  .contact dt, .contact dd { margin: 0; }
  .address {
    position: absolute;
    right: 60px;
    top: 498px;
    font-family: "PT Sans Narrow", sans-serif;
    font-style: normal;
    font-size: 47px;
    line-height: 60px;
    color: var(--paper);
    text-align: right;
  }
</style>
</head>
<body>
<main class="card">
  <svg class="card__band" width="1200" height="686" viewBox="0 0 1200 686" aria-hidden="true">
    <path d="M588,0 C516,96 470,290 552,360 C630,425 700,470 718,686 L1200,686 L1200,0 Z" fill="var(--gold)"/>
  </svg>

  <div class="card__emblem" role="img" aria-label="Golden medical caduceus emblem"></div>

  <div class="logo-box">
    <div class="logo-box__name">Your<br>Logo<br>Here</div>
  </div>

  <ul class="identity">
    <li>Your Name</li>
    <li>Your Position</li>
    <li>Your Title</li>
    <li>Direct Line/Ext.</li>
    <li>Facimail</li>
    <li>E-mail</li>
  </ul>

  <dl class="contact">
    <dt>Toll Free:</dt><dd>1-800-555-6622</dd>
    <dt>Local:</dt><dd>1-333-555-6622</dd>
    <dt>Fax:</dt><dd>1-333-555-6621</dd>
    <dt>E-m@il:</dt><dd>info@yourname.example</dd>
    <dt>Website:</dt><dd>www.yourname.example</dd>
  </dl>

  <address class="address">
    1235 Cool Street # 1<br>
    City Center, CW 11111
  </address>
</main>
</body>
</html>
```